Tolliver Partners
Business Cards, Letterhead, Envelope and 3-4 basic Power Point Slides
Tolliver Partners -
Creative Brief
Please submit designs for: Business Cards, Letterhead, No. 10 Envelope and 3-4 Basic Power Point Slides Please see our web site for more information: TolliverPartners.com
Corporate and Investor Services
We have already completed our logo and its is available for downloading. Please do not make changes to the logo.

```html
<!DOCTYPE html>
<html lang="en">
<head>
<meta charset="utf-8">
<title>Tolliver Partners – PowerPoint Templates</title>
<link rel="stylesheet" href="https://fonts.googleapis.com/css2?family=Arimo:wght@400;700&display=swap">
<style>
  :root {
    --navy: #0b3f93;
    --blue: #1a6fd0;
    --sky: #5db3f0;
    --green: #3f9e2a;
    --lime: #7cc242;
    --ink: #1a1a1a;
    --label: #444;
    --rule: #bdbdbd;
    --paper: #ffffff;
  }
  * { box-sizing: border-box; margin: 0; padding: 0; }
  html, body { width: 1200px; height: 464px; overflow: hidden; background: var(--paper); }
  body { position: relative; font-family: "Arimo", Arial, sans-serif; color: var(--ink); }

  .slide-label { position: absolute; top: 6px; font-size: 12px; color: var(--label); }
  .slide {
    position: absolute; top: 29px; width: 578px; height: 427px;
    border: 1px solid var(--rule); overflow: hidden; background: var(--paper);
  }
  .slide--front { left: 5px; }
  .slide--inside { left: 617px; }
  .slide-art { position: absolute; inset: 0; width: 100%; height: 100%; }

  .brand-name { position: absolute; color: var(--green); font-weight: 700; white-space: nowrap; }
  .brand-name--front { left: 26px; top: 356px; font-size: 26px; }
  .brand-name--inside { right: 18px; top: 50px; font-size: 17px; }

  .front-title {
    position: absolute; left: 388px; top: 356px;
    font-size: 30px; font-weight: 700; color: var(--navy);
  }
  .inside-title {
    position: absolute; left: 30px; top: 100px;
    font-size: 38px; font-weight: 400; color: var(--ink);
  }
  .body-copy {
    position: absolute; left: 30px; top: 150px; width: 318px;
    font-size: 8.6px; line-height: 11.6px; text-align: justify; color: var(--ink);
  }
  .body-copy p + p { margin-top: 9px; }

  .picture-slot {
    position: absolute; left: 362px; width: 196px; height: 98px;
    border: 1px solid #666; display: flex; align-items: center; justify-content: center;
    font-size: 24px; background: var(--paper);
  }
  .picture-slot--upper { top: 180px; }
  .picture-slot--lower { top: 292px; }
</style>
</head>
<body>

<span class="slide-label" style="left:5px">PowerPoint Template Front</span>
<span class="slide-label" style="left:617px">PowerPoint Template Inside</span>

<section class="slide slide--front">
  <svg class="slide-art" viewBox="0 0 578 427" preserveAspectRatio="none">
    <defs>
      <linearGradient id="frontPhotoTone" x1="0" y1="0" x2="1" y2="0.4">
        <stop offset="0" stop-color="#0b3f93"/>
        <stop offset="0.55" stop-color="#1a6fd0"/>
        <stop offset="1" stop-color="#8fd0f7"/>
      </linearGradient>
    </defs>
    <path d="M0,292 C160,256 380,300 578,350 V366 C380,320 160,280 0,312 Z" fill="var(--green)"/>
    <path d="M0,282 C170,246 380,292 578,338 V350 C380,302 160,258 0,294 Z" fill="var(--lime)"/>
    <path d="M0,0 H578 V330 C380,284 170,236 0,276 Z" fill="url(#frontPhotoTone)"
          role="img" aria-label="Photo: business people in silhouette in front of a globe with an airplane"/>
    <path d="M0,276 C170,236 380,284 578,330 V338 C380,292 170,246 0,282 Z" fill="var(--paper)"/>
  </svg>
  <span class="brand-name brand-name--front">Tolliver Partners</span>
  <h1 class="front-title">TITLE</h1>
</section>

<section class="slide slide--inside">
  <svg class="slide-art" viewBox="0 0 578 427" preserveAspectRatio="none">
    <path d="M0,0 H578 V0 C420,30 200,40 0,70 Z" fill="var(--sky)"/>
    <path d="M0,52 C200,24 420,14 578,-4 V4 C420,30 200,44 0,70 Z" fill="var(--blue)"/>
    <path d="M0,70 C200,44 420,30 578,4 V16 C420,44 200,58 0,84 Z" fill="var(--green)"/>
    <path d="M0,410 C140,384 300,418 578,410 V427 H0 Z" fill="var(--blue)"/>
    <path d="M0,402 C140,374 300,410 578,402 V410 C300,418 140,384 0,410 Z" fill="var(--lime)"/>
  </svg>
  <span class="brand-name brand-name--inside">Tolliver Partners</span>
  <h2 class="inside-title">TITLE</h2>
  <div class="body-copy">
    <p>Tolliver Partners provides corporate and investor services to companies at every stage of growth. Our team works closely with management to plan capital strategy, prepare clear reporting and build lasting relationships with shareholders. We combine careful analysis with practical advice so that each decision rests on sound information. From first funding rounds to public listings, we guide clients through each step with steady attention and open communication. Every engagement begins with listening, and every plan is shaped around the goals of the people we serve.</p>
    <p>Our investor services include shareholder outreach, meeting preparation, market feedback and ongoing communication programs. We help companies present their story with clarity and confidence to analysts, funds and private investors. Corporate services cover governance support, board materials and transaction planning. Each program is tailored to the size and needs of the client, with measurable results reviewed at regular intervals. Contact our team to learn how we can support your next stage of growth.</p>
  </div>
  <div class="picture-slot picture-slot--upper">Picture</div>
  <div class="picture-slot picture-slot--lower">Picture</div>
</section>

</body>
</html>
```